Proofreading business card design needed

I need a business card for a proofreading business based in Kempsey.
It is our business to scour our clients' written word finding and fixing errors.
We: protect people, businesses and organisations from
embarrassment,
safeguard brands and reputations,
save time and money on costly mistakes.
Updates

Hi Everyone,

I need to make a change to my motto - if you have used it.  The last line of my motto needs to say: save you time and money by eliminating costly errors
Sorry about this change, almost at the last minute, but the way it's currently written just didn't put across what I was trying to say.
Thanks
Mara

Target Market(s)

self-publishers, businesses and organisations, research and educational publishers

Industry/Entity Type

Business

Contact Information for Business Card

The Quill Check Studio, Mara Tillbrook, Ph: 0471 392 548, Email: mara.check@quillmail.example, www.thequillcheckstudio.example.au, Po Box 5219, East Willowmere, NSW, 2999.

Logo Text

The Quill Check Studio

Logo styles of interest
Abstract Logo
Character Logo
Wordmark Logo
Requirements
Nice to have
• Modern take on proofreading or business images: glasses, written word, red pen or pencil, ruler, magnifying glass etc.
Is it possible to have the following text on the card:
'We: protect people, businesses and organisations from
embarrassment,
save time and money on costly mistakes.'
However, I'm totally open to new ideas/concepts.
Would be happy to see some double-sided business card concepts.

```html
<!DOCTYPE html>
<html lang="en">
<head>
<meta charset="utf-8">
<title>The Quill Check Studio – Business Card</title>
<link rel="stylesheet" href="https://fonts.googleapis.com/css2?family=Oswald:wght@400;500&family=Open+Sans:wght@400;600;700&display=swap">
<style>
  :root {
    --page: #ffffff;
    --front-bg: #04060b;
    --front-dot: #141b24;
    --brand-light: #7fc8f0;
    --motto: #a9c08e;
    --back-bg-top: #dcdcdc;
    --back-bg-bottom: #d2d2d2;
    --ink: #151515;
    --accent-blue: #1a8fd8;
    --panel-dark-a: #0c181b;
    --panel-dark-b: #23344a;
    --mark-blue: #1e86c6;
    --white: #ffffff;
    --shadow: rgba(0, 0, 0, 0.55);
  }
  * { margin: 0; padding: 0; box-sizing: border-box; }
  html, body {
    width: 1200px; height: 1000px; overflow: hidden;
    background: var(--page);
  }
  .sheet { position: relative; width: 1200px; height: 1000px; }

  .card {
    position: absolute;
    overflow: hidden;
    box-shadow: 10px 10px 14px var(--shadow);
  }

  /* Front */
  .card--front {
    left: 247px; top: 77px; width: 701px; height: 405px;
    background: var(--front-bg);
  }
  .front-texture {
    position: absolute; left: 0; top: 90px; width: 701px; height: 315px;
    background: linear-gradient(180deg, transparent 0%, var(--front-dot) 45%, transparent 100%);
    opacity: 0.8;
  }
  .front-mark {
    position: absolute; left: 302px; top: 70px;
    width: 96px; height: 96px; border-radius: 50%;
    background: var(--mark-blue);
  }
  .front-name {
    position: absolute; left: 0; top: 214px; width: 701px;
    text-align: center;
    font-family: "Oswald", sans-serif; font-weight: 500;
    font-size: 23px; letter-spacing: 0.3px;
    color: var(--brand-light); text-transform: uppercase;
  }
  .front-motto {
    position: absolute; left: 0; top: 266px; width: 701px;
    text-align: center;
    font-family: "Open Sans", sans-serif; font-weight: 400;
    font-size: 17.8px; line-height: 23px;
    color: var(--motto); text-transform: uppercase;
    white-space: nowrap;
  }

  /* Back */
  .card--back {
    left: 247px; top: 525px; width: 703px; height: 407px;
    background: linear-gradient(180deg, var(--back-bg-top), var(--back-bg-bottom));
  }
  .back-mark {
    position: absolute; left: 73px; top: 48px;
    width: 90px; height: 90px; border-radius: 50%;
    background: var(--mark-blue);
  }
  .back-brand {
    position: absolute; left: 38px; top: 152px; width: 160px;
    text-align: center;
    font-family: "Oswald", sans-serif; font-weight: 500;
    font-size: 14px; color: var(--ink); text-transform: uppercase;
    white-space: nowrap;
  }
  .back-swoosh { position: absolute; left: 0; top: 0; }
  .holder-name {
    position: absolute; left: 36px; top: 285px;
    font-family: "Open Sans", sans-serif; font-weight: 700;
    font-size: 24px; color: var(--ink); text-transform: uppercase;
    letter-spacing: 0.2px; white-space: nowrap;
  }
  .contact {
    position: absolute; left: 318px; top: 225px; width: 376px;
    list-style: none; text-align: center;
    font-family: "Open Sans", sans-serif; font-weight: 400;
    font-size: 19px; line-height: 30.5px; color: var(--white);
    white-space: nowrap;
  }
</style>
</head>
<body>
<main class="sheet">
  <section class="card card--front" aria-label="Business card front">
    <div class="front-texture" role="img" aria-label="Faint dotted wave texture across the card"></div>
    <div class="front-mark" aria-hidden="true"></div>
    <h1 class="front-name">The Quill Check Studio</h1>
    <p class="front-motto">
      We protect people, businesses and organisations from<br>
      embarrassment,<br>
      safeguard brands and reputations,<br>
      save time and money on costly mistakes
    </p>
  </section>

  <section class="card card--back" aria-label="Business card back">
    <svg class="back-swoosh" width="703" height="407" viewBox="0 0 703 407" aria-hidden="true">
      <defs>
        <linearGradient id="panelDark" x1="0" y1="1" x2="1" y2="0">
          <stop offset="0" stop-color="var(--panel-dark-a)"/>
          <stop offset="1" stop-color="var(--panel-dark-b)"/>
        </linearGradient>
      </defs>
      <path d="M703 0 C560 62 360 182 282 280 C268 302 292 352 365 407 L703 407 Z" fill="var(--accent-blue)"/>
      <path d="M703 8 C572 74 384 192 302 286 C290 306 310 352 380 407 L703 407 Z" fill="url(#panelDark)"/>
    </svg>
    <div class="back-mark" aria-hidden="true"></div>
    <p class="back-brand">The Quill Check Studio</p>
    <h2 class="holder-name">Mara Tillbrook</h2>
    <ul class="contact">
      <li>PH: 0471 392 548</li>
      <li>EMAIL: mara.check@quillmail.example</li>
      <li>www.thequillcheckstudio.example.au</li>
      <li>PO BOX 5219</li>
      <li>EAST WILLOWMERE, NSW, 2999</li>
    </ul>
  </section>
</main>
</body>
</html>
```